Business Card Design

Please visit www.MarkDorsey.com to acquire information for business card.

Back Side of Card:
a lifetime of experience working for you.

With over 25 years in the construction industry, well over a decade as a licensed Subcontractor / General Contractor and nearly 10 years as a licensed Realtor, I have excelled and cultivated a working knowledge of how all the pieces fit together.

Here is a link to folder.
https://files.examplecloud.net/folderview?id=7Qk2mXrTpLw9zVbN4sHcDyUeFaGj&usp=sharing

Industry/Entity Type

Construction

Contact Information for Business Card

Company: Mark Dorsey, LLC.
Address: 31872 W. Cedar Hollow Blvd. Suite 207-418
Name: Mark Dorsey
Phone: (623) 587-2914
Web: www.MarkDorsey.com
Type of services offered: Architectural Design, 3D Models, Renderings & Animation - Construction Documents - Project Managment.

```html
<!DOCTYPE html>
<html lang="en">
<head>
<meta charset="utf-8">
<title>Mark Dorsey, LLC. – Business Card</title>
<link rel="stylesheet" href="https://fonts.googleapis.com/css2?family=Open+Sans:wght@400;700&display=swap">
<style>
  :root {
    --page: #e9e7e3;
    --card: #fafafa;
    --plan-light: #f6f6f5;
    --plan-mid: #d9dadb;
    --plan-dark: #c4c6c8;
    --ink: #1c1c1c;
    --ink-soft: #2e2e2e;
    --frame: #1e1e1e;
    --shadow: rgba(0, 0, 0, 0.28);
  }
  * { box-sizing: border-box; margin: 0; padding: 0; }
  html, body {
    width: 1200px;
    height: 1000px;
    overflow: hidden;
    background: var(--page);
    font-family: "Open Sans", Arial, sans-serif;
    color: var(--ink);
  }
  .sheet {
    position: relative;
    width: 1200px;
    height: 1000px;
  }
  .card {
    position: absolute;
    top: 110px;
    width: 440px;
    height: 770px;
    background: var(--card);
    box-shadow: 0 8px 22px var(--shadow);
    overflow: hidden;
  }
  .card--back { left: 120px; }
  .card--front { left: 640px; }

  .card__plan {
    position: absolute;
    inset: 0;
    background:
      radial-gradient(ellipse 60% 35% at 60% 62%, var(--plan-dark) 0%, transparent 70%),
      radial-gradient(ellipse 55% 30% at 35% 30%, var(--plan-mid) 0%, transparent 70%),
      linear-gradient(160deg, var(--plan-light) 0%, var(--plan-mid) 45%, var(--plan-light) 80%, var(--plan-mid) 100%);
  }

  .brand {
    position: absolute;
    border: 3px solid var(--frame);
    background: #ffffff;
    display: flex;
    align-items: flex-end;
    justify-content: flex-end;
  }
  .brand__name {
    font-weight: 400;
    color: var(--ink);
    white-space: nowrap;
  }

  /* Back side */
  .card--back .brand {
    left: 70px;
    top: 80px;
    width: 300px;
    height: 300px;
    padding: 0 14px 12px 0;
  }
  .card--back .brand__name { font-size: 22px; }
  .tagline {
    position: absolute;
    left: 56px;
    top: 460px;
    font-size: 44px;
    line-height: 1.22;
    color: var(--ink);
  }
  .tagline span { display: block; }
  .tagline span:nth-child(1) { padding-left: 36px; }
  .tagline span:nth-child(2) { padding-left: 66px; }

  /* Front side */
  .card--front .brand {
    right: 34px;
    top: 34px;
    width: 170px;
    height: 170px;
    padding: 0 10px 8px 0;
  }
  .card--front .brand__name { font-size: 13px; }

  .services {
    position: absolute;
    left: 30px;
    right: 30px;
    top: 226px;
    list-style: none;
    font-size: 18px;
    line-height: 1.2;
    text-transform: uppercase;
    text-align: center;
    color: var(--ink-soft);
  }
  .person {
    position: absolute;
    left: 0;
    right: 0;
    top: 370px;
    text-align: center;
  }
  .person__name {
    font-size: 34px;
    font-weight: 700;
    margin-bottom: 12px;
  }
  .contact {
    display: inline-block;
    text-align: left;
    font-size: 24px;
    line-height: 1.3;
  }
  .contact__label { font-weight: 700; }
  .address {
    position: absolute;
    left: 0;
    right: 0;
    top: 590px;
    text-align: center;
    font-style: normal;
    font-size: 23px;
    line-height: 1.3;
  }
  .address__label { font-weight: 700; }
</style>
</head>
<body>
<main class="sheet">

  <section class="card card--back" aria-label="Back of business card">
    <div class="card__plan" role="img" aria-label="Faint grey architectural floor-plan drawing filling the card background"></div>
    <div class="brand">
      <span class="brand__name">Mark Dorsey, LLC.</span>
    </div>
    <p class="tagline">
      <span>a lifetime of</span>
      <span>experience</span>
      <span>working for you.</span>
    </p>
  </section>

  <section class="card card--front" aria-label="Front of business card">
    <div class="card__plan" role="img" aria-label="Faint grey architectural floor-plan drawing filling the card background"></div>
    <div class="brand">
      <span class="brand__name">Mark Dorsey, LLC.</span>
    </div>
    <ul class="services">
      <li>Architectural Design</li>
      <li>3D Models</li>
      <li>Renderings and Animation</li>
      <li>Construction Documents</li>
      <li>Project Management</li>
    </ul>
    <div class="person">
      <p class="person__name">Mark Dorsey</p>
      <p class="contact">
        <span class="contact__label">phone:</span> 623.587.2914<br>
        <span class="contact__label">email:</span> info@markdorsey.com<br>
        www.markdorsey.com
      </p>
    </div>
    <address class="address">
      <span class="address__label">address:</span><br>
      31872 W. Cedar Hollow Blvd<br>
      Suite 207-418<br>
      Ridgefield, Arizona 85390
    </address>
  </section>

</main>
</body>
</html>
```